We are a new company with 2 divisions a medical research and medical product sales. We need a company logo and Business Cards. The design files need to be provided to us in Adobe Photoshop CS 5.1.

Target Market(s)

Medical Community

Industry/Entity Type

Medical

Contact Information for Business Card

Company Name - Larkmoor Biomedical LLC
Company Address 4217 NE 14th Ave Suite 7, Fernhollow Fl 34718

Requirements
Must have
• The design files need to be provided to us in Adobe Photoshop CS 5.1.

```html
<!DOCTYPE html>
<html lang="en">
<head>
<meta charset="utf-8">
<title>Larkmoor Biomedical LLC – Business Card</title>
<link rel="stylesheet" href="https://fonts.googleapis.com/css2?family=Sorts+Mill+Goudy&display=swap">
<style>
  :root {
    --backdrop: #e9e6e1;
    --card-frost: #eeeeec;
    --card-frost-edge: #dcdcd8;
    --brand-green: #1f5a2c;
    --ink-dark: #2a2a2a;
    --ink-grey: #4a4a4a;
    --band-green: #1d4a22;
    --band-green-deep: #123516;
    --lime-light: #c7d86a;
    --lime-deep: #8fa832;
    --mark-green: #7fb33e;
    --contact-rose: #c08b8e;
    --contact-pale: #e4e0dc;
  }
  html, body {
    margin: 0;
    padding: 0;
    width: 1200px;
    height: 970px;
    overflow: hidden;
    background: var(--backdrop);
  }
  .canvas {
    position: relative;
    width: 1200px;
    height: 970px;
  }
  .business-card {
    position: absolute;
    left: 100px;
    top: 207px;
    width: 1000px;
    height: 556px;
    overflow: hidden;
    background: linear-gradient(160deg, var(--card-frost) 0%, var(--card-frost-edge) 100%);
    box-shadow: 0 10px 30px rgba(0,0,0,0.18);
    font-family: "Sorts Mill Goudy", "Times New Roman", serif;
  }
  .card-band {
    position: absolute;
    left: 0;
    top: 0;
    width: 1000px;
    height: 556px;
  }
  .brand {
    position: absolute;
    left: 37px;
    top: 32px;
    display: flex;
    align-items: center;
    gap: 30px;
  }
  .brand-dot {
    width: 160px;
    height: 160px;
    border-radius: 50%;
    background: var(--mark-green);
    flex: none;
  }
  .brand-name {
    margin: 0;
    color: var(--brand-green);
    font-size: 46px;
    font-weight: 400;
    line-height: 1.12;
    letter-spacing: 0.5px;
    text-transform: uppercase;
  }
  .holder {
    position: absolute;
    left: 0;
    width: 1000px;
    top: 218px;
    text-align: center;
  }
  .holder-name {
    margin: 0;
    color: var(--ink-dark);
    font-size: 31px;
    font-weight: 400;
    letter-spacing: 1px;
    line-height: 1.1;
  }
  .holder-title {
    margin: 2px 0 0;
    color: var(--ink-grey);
    font-size: 21px;
    letter-spacing: 0.5px;
  }
  .contact {
    position: absolute;
    margin: 0;
    font-style: normal;
    font-size: 27px;
    line-height: 33px;
  }
  .contact-address {
    left: 37px;
    top: 428px;
    color: var(--contact-rose);
  }
  .contact-online {
    left: 486px;
    top: 458px;
    color: var(--contact-pale);
  }
  .contact-label {
    color: var(--contact-rose);
  }
</style>
</head>
<body>
<div class="canvas">
  <section class="business-card" aria-label="Larkmoor Biomedical LLC business card">
    <svg class="card-band" viewBox="0 0 1000 556" aria-hidden="true">
      <defs>
        <linearGradient id="lime-stripe" x1="0" y1="0" x2="1" y2="0">
          <stop offset="0" stop-color="var(--lime-deep)"/>
          <stop offset="0.6" stop-color="var(--lime-light)"/>
          <stop offset="1" stop-color="var(--lime-deep)"/>
        </linearGradient>
        <linearGradient id="green-band" x1="0" y1="0" x2="0" y2="1">
          <stop offset="0" stop-color="var(--band-green)"/>
          <stop offset="1" stop-color="var(--band-green-deep)"/>
        </linearGradient>
      </defs>
      <path d="M0,286 C260,300 560,330 1000,368 L1000,556 L0,556 Z" fill="url(#lime-stripe)"/>
      <path d="M0,298 C320,322 560,392 760,384 C860,380 940,374 1000,372 L1000,556 L0,556 Z" fill="url(#green-band)"/>
    </svg>

    <header class="brand">
      <span class="brand-dot" aria-hidden="true"></span>
      <h1 class="brand-name">Larkmoor<br>Biomedical LLC.</h1>
    </header>

    <div class="holder">
      <p class="holder-name">EVAN MARSH</p>
      <p class="holder-title">CHIEF EXECUTIVE OFFICER</p>
    </div>

    <address class="contact contact-address">
      4217 NE 14th Ave Suite 7<br>
      Fernhollow Fl 34718<br>
      Phone: 123 456 789
    </address>

    <p class="contact contact-online">
      <span class="contact-label">Email:</span> yourname@yourcompany.com<br>
      www.yourcompany.com
    </p>
  </section>
</div>
</body>
</html>
```